Construction material supplies company business card ****

1. Full company name “Marlow Aggregate Products Ltd”
I am after a Business card design for the company as a whole. We are better known in Solomon Islands as “Marlow Aggregate” for short.

We are a building materials supplier of
Ready Mixed Concrete, Bricks and Blocks,
Quarry products- gravel, aggregates, sand etc.
Cement distributor/retailer of reputable brands.
Other prefab concrete products. Culverts, wave breakers, concrete retaining blocks etc.

2. Competitive Advantage over Competition: Quality, efficient, professional, dependable, reliable

3. We want people to feel trust worthy, high quality, strong when they see our brand

5. No preference to color. Maybe more sturdy and corporate. Not fancy.

Industry/Entity Type

CONSTRUCTION SUPPLY

Contact Information for Business Card

Name, Position, office phone mob phone, email

Requirements
Must have
• the company logo
Nice to have
• would like to see a mixture of designs, of with logo only and also with simple graphic designs to bring out the company whilst still have the strong sturdy professional feeling

```html
<!DOCTYPE html>
<html lang="en">
<head>
<meta charset="utf-8">
<title>Marlow Aggregate – Business Card</title>
<link rel="stylesheet" href="https://fonts.googleapis.com/css2?family=Roboto:wght@400;500;700&display=swap">
<style>
  :root {
    --page-bg: #2a2a2a;
    --navy: #17416b;
    --front-top: #34587f;
    --front-bottom: #284a70;
    --band: rgba(10, 35, 68, 0.55);
    --card-light: #e6e7e8;
    --white: #ffffff;
    --text-light: #e9eef4;
  }
  * { margin: 0; padding: 0; box-sizing: border-box; }
  html, body { width: 1200px; height: 1138px; overflow: hidden; }
  body {
    background: var(--page-bg);
    font-family: "Roboto", Arial, sans-serif;
    position: relative;
  }
  .card {
    position: absolute;
    border-radius: 14px;
    overflow: hidden;
    box-shadow: 0 4px 10px rgba(0,0,0,0.45);
  }

  /* Front */
  .card-front {
    left: 274px; top: 186px; width: 623px; height: 376px;
    background: linear-gradient(160deg, var(--front-top), var(--front-bottom));
    color: var(--text-light);
    text-align: center;
  }
  .brand {
    position: absolute; left: 0; right: 0; top: 74px;
    display: flex; align-items: center; justify-content: center; gap: 16px;
    color: var(--white);
  }
  .brand-square {
    width: 54px; height: 54px; border: 6px solid var(--white);
  }
  .brand-name {
    font-weight: 500; font-size: 36px; letter-spacing: 1px;
    text-transform: uppercase;
  }
  .intro-pill {
    position: absolute; left: 137px; top: 186px; width: 349px; height: 40px;
    border-radius: 20px;
    background: rgba(20, 50, 88, 0.7);
    border: 1px solid rgba(255,255,255,0.18);
    font-size: 16px; line-height: 38px; color: var(--white);
    z-index: 1;
  }
  .offer-band {
    position: absolute; left: 0; right: 0; top: 214px; height: 78px;
    background: var(--band);
    padding-top: 21px;
    font-size: 16px; line-height: 22px;
  }
  .offer-more {
    position: absolute; left: 0; right: 0; top: 304px;
    font-size: 16px; line-height: 25px;
  }

  /* Back */
  .card-back {
    left: 276px; top: 608px; width: 618px; height: 374px;
    background: var(--card-light);
    color: var(--navy);
  }
  .wave { position: absolute; left: 0; top: 0; }
  .values {
    position: absolute; right: 36px; top: 22px;
    text-align: right; color: var(--white);
    font-size: 16px; line-height: 24px;
  }
  .person { position: absolute; left: 42px; top: 112px; }
  .person-name { font-size: 22px; font-weight: 700; line-height: 28px; }
  .person-role { font-size: 16px; line-height: 22px; }
  .contacts {
    position: absolute; left: 42px; top: 203px;
    list-style: none; font-size: 16px;
  }
  .contacts li { display: flex; align-items: center; height: 26px; }
  .contacts svg { width: 14px; height: 14px; margin-right: 18px; fill: var(--navy); }
  .address { position: absolute; left: 42px; top: 292px; font-size: 16px; line-height: 26px; }
  .back-brand {
    position: absolute; left: 330px; width: 256px; top: 200px;
    display: flex; flex-direction: column; align-items: center; gap: 14px;
  }
  .back-brand .brand-square { border-color: var(--navy); width: 62px; height: 62px; border-width: 7px; }
  .back-brand .brand-name { font-size: 24px; color: var(--navy); }
</style>
</head>
<body>

<section class="card card-front">
  <div class="brand">
    <span class="brand-square"></span>
    <span class="brand-name">Marlow Aggregate</span>
  </div>
  <div class="intro-pill">We are a building materials supplier of</div>
  <div class="offer-band">
    <p>Ready Mixed Concrete, Bricks and Blocks, Quarry Products</p>
    <p>Quarry Products:- Gravel, Aggregates, Sand Etc.</p>
  </div>
  <div class="offer-more">
    <p>Cement Distributor/Retailer of Reputable Brands.</p>
    <p>Other Concrete Products Culverts, Wave Breakers, Concrete Retaining Blocks</p>
  </div>
</section>

<section class="card card-back">
  <svg class="wave" width="618" height="374" viewBox="0 0 618 374" aria-hidden="true">
    <path fill="#17416b" d="M0,0 H618 V106 C570,118 520,128 470,118 C400,104 330,30 240,22 C150,14 60,42 0,72 Z"/>
    <path fill="#e6e7e8" d="M0,56 C70,26 160,10 240,18 C330,28 390,90 470,106 C530,118 580,108 618,96 V104 C580,116 530,124 470,114 C390,98 330,38 240,28 C160,20 70,36 0,66 Z"/>
    <path fill="#17416b" d="M50,70 C130,40 220,36 300,70 C380,104 420,136 480,130 C540,124 590,110 618,100 V112 C590,124 540,140 480,144 C410,146 370,114 300,84 C220,52 130,52 50,70 Z"/>
  </svg>
  <div class="values">
    <p>Quality &nbsp;|&nbsp; Efficient</p>
    <p>Dependable &nbsp;|&nbsp; Reliable</p>
    <p>Professional</p>
  </div>
  <div class="person">
    <p class="person-name">Daniel Hartley</p>
    <p class="person-role">Managing Director</p>
  </div>
  <ul class="contacts">
    <li><svg viewBox="0 0 16 16"><path d="M2 5c0-2 2-3 6-3s6 1 6 3v1h-3V5H5v1H2z M4 7h8l2 6v1H2v-1z"/></svg>000 0000 0000</li>
    <li><svg viewBox="0 0 16 16"><path d="M1 3h14v10H1z M2 4l6 5 6-5v1l-6 5-6-5z" fill-rule="evenodd"/></svg>daniel@marlowaggregate.com</li>
    <li><svg viewBox="0 0 16 16"><circle cx="8" cy="8" r="7"/></svg>www.marlowaggregate.com</li>
  </ul>
  <p class="address">18 Harbour Rd., Kerrow,<br>Westfield, US 40517</p>
  <div class="back-brand">
    <span class="brand-square"></span>
    <span class="brand-name">MARLOW AGGREGATE</span>
  </div>
</section>

</body>
</html>
```